Corporate brochure Velorin consulting

I am a business law and taxation law firm. I would like to create a super sharp and modern catalogue that really describes our values and the services we offer among other things. It has to be bilingual. I dont want it to look like old fashioned typical law firms. Here are some characteristics of the catalogue:

- size: 8.5 x 11 landscape
- 20 pages in total including the cover page
- bilingual catalogue

Our corporate colors are the ones used in the logo attached.

I already have purchased all of the photos needed for the project.Please see attached document for a detailed description of the project.

I have pictures that I can email you for the project. just email me at jbarlow@velorin-example.ca and I will send the file.

I would just like for you to make available the text boxes on each page and then I will provide the text once Im finished.

Target Market(s)

business owners and professionals

Industry/Entity Type

Business

Font styles to use
Sans Serif

Colors
0692cd
f37122

Requirements
Must have
• bold fonts, very clean white backgrounds, modern and yet very edgy design
• each page should have a large enough area to add text.
• ***I like as the titles: all in large letters and font to use is Adequate,
• Large titles on the left side of page in orange and right side in blue
• for the text: font to be used is asenine
• page numbering should be very visible in the middle of the page left and right and not on bottom or upper corners.
Nice to have
• I like the use of metallic silvers . Not all of the pictures need to be used its the choic of the designer.

```html
<!DOCTYPE html>
<html lang="en">
<head>
<meta charset="utf-8">
<title>Velorin – About</title>
<link href="https://fonts.googleapis.com/css2?family=Arimo:wght@400;700&display=swap" rel="stylesheet">
<style>
  :root {
    --velorin-blue: #0692cd;
    --velorin-orange: #f37122;
    --page-bg: #f3f8fc;
    --ink: #33383d;
    --band-fill: rgba(6, 146, 205, 0.32);
    --visual-light: #c9d8ef;
    --visual-mid: #a9c0e6;
  }
  html, body {
    margin: 0;
    padding: 0;
    width: 1200px;
    height: 800px;
    overflow: hidden;
    background: var(--page-bg);
    font-family: "Arimo", Arial, sans-serif;
  }
  .page {
    position: relative;
    width: 1200px;
    height: 800px;
    background: var(--page-bg);
    overflow: hidden;
  }
  .cycle-visual {
    position: absolute;
    left: 240px;
    top: 40px;
    width: 720px;
    height: 720px;
    background: linear-gradient(160deg, var(--visual-light) 0%, var(--visual-mid) 100%);
  }
  .about-band {
    position: absolute;
    left: 110px;
    top: 330px;
    width: 980px;
    height: 210px;
    border-radius: 14px;
    background: var(--band-fill);
  }
  .about-title {
    position: absolute;
    left: 140px;
    top: 272px;
    margin: 0;
    font-size: 46px;
    line-height: 56px;
    font-weight: 700;
    letter-spacing: 1px;
    color: var(--velorin-orange);
  }
  .about-text {
    position: absolute;
    left: 140px;
    top: 352px;
    width: 920px;
    margin: 0;
    font-size: 20px;
    font-weight: 700;
    line-height: 1.3;
    color: var(--ink);
  }
  .about-text p {
    margin: 0 0 20px 0;
  }
  .brand {
    position: absolute;
    right: 70px;
    bottom: 70px;
    display: flex;
    align-items: center;
    gap: 12px;
  }
  .brand-square {
    width: 26px;
    height: 26px;
    background: var(--velorin-orange);
  }
  .brand-name {
    font-size: 40px;
    font-weight: 700;
    color: var(--velorin-blue);
  }
</style>
</head>
<body>
  <main class="page">
    <div class="cycle-visual" role="img" aria-label="Photo area: blue 3D arrows forming a circular process cycle around small gears"></div>

    <div class="about-band"></div>
    <h1 class="about-title">ABOUT</h1>
    <div class="about-text">
      <p>Since the creation of Velorin Conseils Inc., our tax lawyers have promoted a modern approach, constantly questioning the traditional practice of law, to put the customer at the center of their concerns.</p>
      <p>Professionalism, attention to customer service, rigor and thoroughness of our tax lawyers guarantee the quality of our work.</p>
    </div>

    <div class="brand">
      <span class="brand-square"></span>
      <span class="brand-name">Velorin</span>
    </div>
  </main>
</body>
</html>
```